Marketing firm Studio 847
Business card and stationery
Project: Marketing firm Studio 847
Marketing firm Studio 847  -
Creative Brief
Professional
Martin Kovalenko
Marketer, Business Strategist
Derveni, 14, 2385, Strovolia Marenvale Ostria
Martin@studio-847.com
Www.studio-847.com
I need the logo and the dog on both, business cards and stationery. I need embossed logo or dog but I am also open to other designs.
He logo and the dog but I am also open to new design

```html
<!DOCTYPE html>
<html lang="en">
<head>
<meta charset="utf-8">
<title>Studio 847 — Stationery Set</title>
<link href="https://fonts.googleapis.com/css2?family=Arimo:wght@400;700&display=swap" rel="stylesheet">
<style>
  :root{
    --purple:#8d56a9;
    --purple-deep:#7a4496;
    --ink:#1a1a1a;
    --paper:#ffffff;
    --frame:#9a9a9a;
    --ghost:#e4e4e4;
    --card-black:#1c1a1c;
  }
  html,body{margin:0;padding:0;overflow:hidden;}
  body{width:1200px;height:734px;background:var(--paper);font-family:'Arimo',Arial,sans-serif;color:var(--ink);position:relative;}
  .sheet-frame{position:absolute;left:4px;top:4px;width:1190px;height:724px;border:1px solid var(--frame);box-sizing:border-box;}
  .piece{position:absolute;overflow:hidden;background:var(--paper);box-shadow:0 0 0 1px #c9c9c9;}
  .piece svg.bg{position:absolute;left:0;top:0;}
  .brand{position:absolute;font-weight:700;letter-spacing:1px;white-space:nowrap;display:flex;align-items:center;gap:6px;}
  .brand .dot{display:inline-block;border-radius:50%;}
  .ghost-brand{position:absolute;font-weight:700;color:var(--ghost);white-space:nowrap;letter-spacing:2px;}

  /* Letterhead */
  .letterhead{left:24px;top:43px;width:488px;height:666px;}
  .letterhead .brand{left:24px;top:34px;font-size:28px;color:var(--ink);}
  .letterhead .brand .dot{width:9px;height:9px;background:var(--purple);}
  .letterhead .footer{position:absolute;left:24px;top:598px;font-size:8.5px;line-height:12px;}
  .letterhead .footer .accent{color:var(--purple);}
  .letterhead .ghost-brand{right:12px;bottom:6px;font-size:30px;}

  /* Business card, contact side */
  .card-front{left:547px;top:46px;width:202px;height:128px;background:var(--purple);}
  .card-front .name{position:absolute;left:104px;top:20px;font-size:8px;color:#fff;line-height:10px;}
  .card-front .name small{display:block;font-size:5.5px;opacity:.9;}
  .card-front .contact{position:absolute;left:10px;top:46px;font-size:5.5px;line-height:8px;color:#fff;}

  /* Business card, brand side purple */
  .card-purple{left:547px;top:182px;width:202px;height:134px;background:var(--purple);}
  .card-purple .brand{left:36px;top:52px;font-size:22px;color:#fff;}
  .card-purple .brand .dot{width:7px;height:7px;background:var(--ink);}

  /* Business card backs */
  .card-black{left:762px;top:226px;width:202px;height:134px;background:var(--card-black);}
  .card-black .brand{left:30px;top:52px;font-size:22px;color:#fff;}
  .card-black .brand .dot{width:7px;height:7px;background:var(--purple);}
  .card-white{left:976px;top:240px;width:202px;height:120px;}
  .card-white .brand{left:30px;top:46px;font-size:22px;color:var(--ink);}
  .card-white .brand .dot{width:7px;height:7px;background:var(--purple);}

  /* Envelope */
  .envelope{left:547px;top:377px;width:631px;height:338px;}
  .envelope .flap-brand{left:235px;top:12px;font-size:18px;color:#fff;transform:rotate(180deg);}
  .envelope .flap-brand .dot{width:6px;height:6px;background:var(--ink);}
  .envelope .brand.main{left:20px;top:118px;font-size:28px;color:#fff;}
  .envelope .brand.main .dot{width:9px;height:9px;background:var(--ink);}
  .envelope .return-address{position:absolute;left:20px;top:206px;font-size:8.5px;}
  .envelope .ghost-brand{right:14px;bottom:6px;font-size:38px;}
</style>
</head>
<body>
<div class="sheet-frame"></div>

<section class="piece letterhead" aria-label="Letterhead">
  <svg class="bg" width="488" height="666" viewBox="0 0 488 666" aria-hidden="true">
    <path d="M0 0H488V240Q300 40 0 100Z" fill="var(--purple)"/>
    <path d="M0 100Q300 40 488 240" fill="none" stroke="var(--ink)" stroke-width="3"/>
  </svg>
  <div class="brand">STUDIO 847<span class="dot"></span></div>
  <div class="footer">
    <div>Derveni, 14, 2385, Strovolia Marenvale Ostria</div>
    <div class="accent">Cell: 99 555 0182 | Phone: 22 555 0147</div>
    <div class="accent">Email: Martin@studio-847.com | Www.studio-847.com</div>
  </div>
  <div class="ghost-brand">STUDIO 847</div>
</section>

<section class="piece card-front" aria-label="Business card contact side">
  <svg class="bg" width="202" height="128" viewBox="0 0 202 128" aria-hidden="true">
    <path d="M0 128V105Q110 95 202 60V128Z" fill="#9d6bb6"/>
  </svg>
  <div class="name">Martin Kovalenko<small>Marketer, Business Strategist</small></div>
  <div class="contact">
    Derveni, 14, 2385, Strovolia Marenvale Ostria<br>
    Tel: 22 555 0147<br>
    Cell: 99 555 0182<br>
    Fax: 22 555 0148<br>
    Martin@studio-847.com
  </div>
</section>

<section class="piece card-purple" aria-label="Business card brand side">
  <div class="brand">STUDIO 847<span class="dot"></span></div>
</section>

<section class="piece card-black" aria-label="Business card back, dark">
  <div class="brand">STUDIO 847<span class="dot"></span></div>
</section>

<section class="piece card-white" aria-label="Business card back, light">
  <div class="brand">STUDIO 847<span class="dot"></span></div>
</section>

<section class="piece envelope" aria-label="Envelope">
  <svg class="bg" width="631" height="338" viewBox="0 0 631 338" aria-hidden="true">
    <path d="M0 0H631V80Q320 90 0 182Z" fill="var(--purple)"/>
    <path d="M0 182Q320 90 631 80" fill="none" stroke="var(--ink)" stroke-width="3"/>
  </svg>
  <div class="brand flap-brand">STUDIO 847<span class="dot"></span></div>
  <div class="brand main">STUDIO 847<span class="dot"></span></div>
  <div class="return-address">Derveni, 14, 2385, Strovolia Marenvale Ostria</div>
  <div class="ghost-brand">STUDIO 847</div>
</section>
</body>
</html>
```